Redesign our iOS App Design mockups

- Redesign our current Zelvo App Mockup
- Keep the design simple so that programmers do not have to do too much extra work to make your design work.
- Look at the attached website screenshot for the overall look and feel, and color scheme
- Convert the attached vector logo to iOS Icon format.
- Deliver all graphics in the density required for Zelvo QT Grand.
- I have attached the current iOS mockup in a .ZIP file but you can view it here as well: https://boards.kelmoraview.com/share/TRWQBN8HDK2

Target Market(s)

Mostly Male Internet Consumers between the ages of 20 and 35

Industry/Entity Type

Internet

Colors

Designer to choose colors to be used in the design.

Requirements
Must have
• - Deliver all graphics in the density required for Zelvo QT Grand
• - Should also look good on Murel and Murel pro
• - Design type should be “FLAT.”
• - Spell out fonts used in the design and where they are used. Also, include font sizes.
• - Please use ALL the elements in each page and use all placements and text EXACTLY. Please do not improvise with text or components.
• I have designed the mockup exactly the way I like it. I just want it to made to look better.
Should not have

```html
<!DOCTYPE html>
<html lang="en">
<head>
<meta charset="utf-8">
<title>NestraVPN – iOS App Screens</title>
<link rel="stylesheet" href="https://fonts.googleapis.com/css2?family=Montserrat:wght@400;600;700;800&family=Inter:wght@400;500;600&display=swap">
<style>
  :root {
    --coral: #f25c4c;
    --canvas: #ffffff;
    --screen-grey: #efeff4;
    --bar-white: #f9f9f9;
    --frame: #d6d6d6;
    --ink: #111111;
    --ink-soft: #333333;
    --ios-blue: #2f7cf6;
    --field: #e8e8e8;
    --field-text: #a5a5a5;
    --row-divider: #dcdcdc;
  }
  * { box-sizing: border-box; margin: 0; padding: 0; }
  html, body { width: 1200px; height: 533px; overflow: hidden; background: var(--canvas); }
  body { position: relative; font-family: "Montserrat", sans-serif; color: var(--ink); line-height: 1.2; }

  .screen { position: absolute; top: 37px; height: 461px; overflow: hidden; background: var(--coral); }
  .screen--splash { left: 46px; width: 201px; background: var(--screen-grey); border: 1px solid var(--frame); }
  .screen--login { left: 270px; width: 201px; background: var(--screen-grey); border: 1px solid var(--frame); }
  .screen--forgot { left: 494px; width: 211px; }
  .screen--settings { left: 717px; width: 212px; }
  .screen--protocols { left: 941px; width: 212px; }

  .status-bar { position: absolute; left: 0; top: 0; width: 100%; height: 24px; background: var(--bar-white); }
  .status-bar__time { position: absolute; left: 18px; top: 7px; font-family: "Inter", sans-serif; font-weight: 600; font-size: 8.5px; line-height: 10px; }
  .status-bar__icons { position: absolute; right: 12px; top: 9px; }

  .nav-bar { position: absolute; left: 0; top: 24px; width: 100%; height: 26px; background: var(--bar-white); border-bottom: 1px solid #e2e2e2; font-family: "Inter", sans-serif; }
  .nav-bar__title { position: absolute; left: 0; right: 0; top: 8px; text-align: center; font-size: 9px; line-height: 11px; font-weight: 600; }
  .nav-bar__back { position: absolute; left: 5px; top: 9px; font-size: 6px; line-height: 8px; color: var(--ios-blue); display: flex; align-items: center; gap: 2px; }

  /* brand wordmark */
  .brand { position: absolute; left: 0; right: 0; display: flex; flex-direction: column; align-items: center; }
  .brand__dot { border-radius: 50%; background: var(--coral); }
  .brand__name { font-weight: 600; color: var(--ink-soft); letter-spacing: 0.5px; }
  .screen--splash .brand { top: 160px; gap: 18px; }
  .screen--splash .brand__dot { width: 64px; height: 64px; }
  .screen--splash .brand__name { font-size: 17px; line-height: 20px; }
  .screen--login .brand { top: 118px; gap: 10px; }
  .screen--login .brand__dot { width: 40px; height: 40px; }
  .screen--login .brand__name { font-size: 10.5px; line-height: 13px; }

  .loader { position: absolute; left: 62px; top: 289px; width: 89px; height: 2px; background: var(--ink); }
  .loader__fill { width: 34px; height: 100%; background: var(--coral); }

  /* forms */
  .login-card { position: absolute; left: 23px; top: 207px; width: 166px; height: 120px; background: var(--coral); padding: 24px 0 0 21px; }
  .field-label { display: block; font-size: 4.5px; line-height: 6px; font-weight: 700; color: #fff; text-transform: uppercase; margin-bottom: 2px; }
  .field { width: 126px; height: 11px; background: var(--field); font-size: 4.5px; line-height: 11px; color: var(--field-text); padding: 0 3px; margin-bottom: 12px; overflow: hidden; white-space: nowrap; }
  .button { display: block; height: 11px; background: var(--field); color: var(--coral); font-size: 4.5px; font-weight: 700; text-transform: uppercase; text-align: center; line-height: 11px; letter-spacing: 0.3px; white-space: nowrap; }
  .login-card .button { width: 88px; margin-left: 19px; margin-top: -3px; }
  .text-link { position: absolute; font-size: 4.8px; line-height: 6px; font-weight: 700; color: var(--coral); text-decoration: underline; text-transform: uppercase; }
  .login-forgot { left: 44px; top: 335px; }
  .signup-note { position: absolute; left: 0; right: 0; top: 426px; text-align: center; font-size: 5px; line-height: 7px; font-weight: 700; text-decoration: underline; }
  .signup-note span { color: var(--coral); text-transform: uppercase; }

  .forgot { position: absolute; left: 16px; top: 70px; width: 180px; color: #fff; }
  .forgot__title { font-size: 10.5px; line-height: 13px; font-weight: 800; margin-bottom: 3px; }
  .forgot__intro { font-size: 4.6px; font-weight: 700; line-height: 6.6px; margin-bottom: 16px; }
  .forgot .field { width: 124px; margin-bottom: 12px; }
  .forgot .button { width: 124px; }

  /* settings lists */
  .section-title { position: absolute; left: 16px; top: 80px; font-size: 7px; line-height: 9px; font-weight: 600; color: #fff; text-transform: uppercase; }
  .settings-panel { position: absolute; left: 0; top: 101px; width: 100%; background: var(--screen-grey); }
  .setting-row { display: flex; align-items: center; gap: 6px; padding: 0 16px; height: 20px; border-top: 1px solid var(--row-divider); font-size: 6px; line-height: 8px; font-weight: 600; }
  .setting-row--toggle { height: 38px; border-top: 0; align-items: flex-start; padding-top: 6px; justify-content: space-between; }
  .setting-row__name { color: var(--coral); font-size: 7px; line-height: 9px; font-weight: 600; text-transform: uppercase; }
  .setting-row__desc { font-size: 6px; font-weight: 600; line-height: 8px; width: 140px; }
  .toggle { flex: none; width: 29px; height: 18px; border-radius: 9px; background: var(--coral); position: relative; margin-top: 4px; }
  .toggle::after { content: ""; position: absolute; right: 2px; top: 2px; width: 14px; height: 14px; border-radius: 50%; background: #fff; }
  .legal { position: absolute; left: 16px; top: 414px; font-size: 5px; font-weight: 700; color: #fff; line-height: 9px; }
  .legal a { display: block; color: #fff; text-decoration: underline; }

  .protocol-list { position: absolute; left: 0; top: 101px; width: 100%; list-style: none; }
  .protocol { display: block; position: relative; height: 29px; border-top: 1px solid var(--row-divider); background: var(--coral); }
  .protocol:first-child { background: var(--screen-grey); border-top: 0; }
  .protocol__name { position: absolute; left: 16px; top: 4px; font-size: 7px; line-height: 9px; font-weight: 700; color: #fff; white-space: nowrap; }
  .protocol:first-child .protocol__name { color: var(--coral); }
  .protocol__desc { position: absolute; left: 16px; top: 14px; font-size: 6px; line-height: 8px; font-weight: 700; color: var(--ink); white-space: nowrap; }
</style>
</head>
<body>

<!-- Splash -->
<section class="screen screen--splash" aria-label="Splash screen">
  <div class="status-bar">
    <span class="status-bar__time">9:41</span>
    <svg class="status-bar__icons" width="30" height="7" viewBox="0 0 30 7" aria-hidden="true">
      <rect x="0" y="5" width="1.4" height="2"/><rect x="2.2" y="3.5" width="1.4" height="3.5"/><rect x="4.4" y="2" width="1.4" height="5"/><rect x="6.6" y="0.5" width="1.4" height="6.5"/>
      <path d="M13.5 6.5l-1.2-1.3a1.8 1.8 0 012.4 0zM11.4 4.3a3 3 0 014.2 0l.6-.7a4 4 0 00-5.4 0zM10.2 3a4.8 4.8 0 016.6 0l.6-.7a5.8 5.8 0 00-7.8 0z"/>
      <rect x="19.5" y="0.8" width="9" height="5.4" rx="1.2" fill="none" stroke="#111" stroke-width="0.7"/><rect x="20.5" y="1.8" width="7" height="3.4" rx="0.5"/><rect x="29" y="2.6" width="0.8" height="1.8"/>
    </svg>
  </div>
  <div class="brand"><span class="brand__dot"></span><span class="brand__name">NESTRAVPN</span></div>
  <div class="loader"><div class="loader__fill"></div></div>
</section>

<!-- Login -->
<section class="screen screen--login" aria-label="Login screen">
  <div class="status-bar">
    <span class="status-bar__time">9:41</span>
    <svg class="status-bar__icons" width="30" height="7" viewBox="0 0 30 7" aria-hidden="true">
      <rect x="0" y="5" width="1.4" height="2"/><rect x="2.2" y="3.5" width="1.4" height="3.5"/><rect x="4.4" y="2" width="1.4" height="5"/><rect x="6.6" y="0.5" width="1.4" height="6.5"/>
      <path d="M13.5 6.5l-1.2-1.3a1.8 1.8 0 012.4 0zM11.4 4.3a3 3 0 014.2 0l.6-.7a4 4 0 00-5.4 0zM10.2 3a4.8 4.8 0 016.6 0l.6-.7a5.8 5.8 0 00-7.8 0z"/>
      <rect x="19.5" y="0.8" width="9" height="5.4" rx="1.2" fill="none" stroke="#111" stroke-width="0.7"/><rect x="20.5" y="1.8" width="7" height="3.4" rx="0.5"/><rect x="29" y="2.6" width="0.8" height="1.8"/>
    </svg>
  </div>
  <div class="nav-bar"><div class="nav-bar__title">Login</div></div>
  <div class="brand"><span class="brand__dot"></span><span class="brand__name">NESTRAVPN</span></div>
  <form class="login-card">
    <label class="field-label">User ID:</label>
    <div class="field">example@postbox.net</div>
    <label class="field-label">Password:</label>
    <div class="field"></div>
    <span class="button">Submit</span>
  </form>
  <a class="text-link login-forgot">Forgot Password</a>
  <p class="signup-note">Dont have an account yet? <span>Sign up here</span></p>
</section>

<!-- Forgot password -->
<section class="screen screen--forgot" aria-label="Forgot password screen">
  <div class="status-bar">
    <span class="status-bar__time">9:41</span>
    <svg class="status-bar__icons" width="30" height="7" viewBox="0 0 30 7" aria-hidden="true">
      <rect x="0" y="5" width="1.4" height="2"/><rect x="2.2" y="3.5" width="1.4" height="3.5"/><rect x="4.4" y="2" width="1.4" height="5"/><rect x="6.6" y="0.5" width="1.4" height="6.5"/>
      <path d="M13.5 6.5l-1.2-1.3a1.8 1.8 0 012.4 0zM11.4 4.3a3 3 0 014.2 0l.6-.7a4 4 0 00-5.4 0zM10.2 3a4.8 4.8 0 016.6 0l.6-.7a5.8 5.8 0 00-7.8 0z"/>
      <rect x="19.5" y="0.8" width="9" height="5.4" rx="1.2" fill="none" stroke="#111" stroke-width="0.7"/><rect x="20.5" y="1.8" width="7" height="3.4" rx="0.5"/><rect x="29" y="2.6" width="0.8" height="1.8"/>
    </svg>
  </div>
  <div class="nav-bar">
    <span class="nav-bar__back"><svg width="4" height="7" viewBox="0 0 4 7" aria-hidden="true"><path d="M3.5 .5L.8 3.5l2.7 3" fill="none" stroke="#2f7cf6" stroke-width="0.9"/></svg>Login Page</span>
    <div class="nav-bar__title">Forgot Password</div>
  </div>
  <div class="forgot">
    <h1 class="forgot__title">Did you forget your Password?</h1>
    <p class="forgot__intro">If you have forgotten your password, enter the email address associated with your account into the box below and we will send you instructions on how to reset your password to your email account.</p>
    <label class="field-label">Email Address:</label>
    <div class="field">example@postbox.net</div>
    <span class="button">Submit Password Reset Request</span>
  </div>
</section>

<!-- Settings -->
<section class="screen screen--settings" aria-label="Settings screen">
  <div class="status-bar">
    <span class="status-bar__time">9:41</span>
    <svg class="status-bar__icons" width="30" height="7" viewBox="0 0 30 7" aria-hidden="true">
      <rect x="0" y="5" width="1.4" height="2"/><rect x="2.2" y="3.5" width="1.4" height="3.5"/><rect x="4.4" y="2" width="1.4" height="5"/><rect x="6.6" y="0.5" width="1.4" height="6.5"/>
      <path d="M13.5 6.5l-1.2-1.3a1.8 1.8 0 012.4 0zM11.4 4.3a3 3 0 014.2 0l.6-.7a4 4 0 00-5.4 0zM10.2 3a4.8 4.8 0 016.6 0l.6-.7a5.8 5.8 0 00-7.8 0z"/>
      <rect x="19.5" y="0.8" width="9" height="5.4" rx="1.2" fill="none" stroke="#111" stroke-width="0.7"/><rect x="20.5" y="1.8" width="7" height="3.4" rx="0.5"/><rect x="29" y="2.6" width="0.8" height="1.8"/>
    </svg>
  </div>
  <div class="nav-bar">
    <span class="nav-bar__back"><svg width="4" height="7" viewBox="0 0 4 7" aria-hidden="true"><path d="M3.5 .5L.8 3.5l2.7 3" fill="none" stroke="#2f7cf6" stroke-width="0.9"/></svg>Settings</span>
    <div class="nav-bar__title">Protocols</div>
  </div>
  <h2 class="section-title">App Settings</h2>
  <div class="settings-panel">
    <div class="setting-row setting-row--toggle">
      <div><div class="setting-row__name">Kill Switch</div><div class="setting-row__desc">Cuts internet connectivity when your VPN connection gets lost</div></div>
      <span class="toggle" role="switch" aria-checked="true"></span>
    </div>
    <div class="setting-row">
      <svg width="12" height="10" viewBox="0 0 12 10" aria-hidden="true"><path d="M6.5 1.5A3.6 3.6 0 102 6.8M6.5 8.5A3.6 3.6 0 012 3.2" fill="none" stroke="#f25c4c" stroke-width="1.1"/><path d="M4 5h7M9 3l2 2-2 2" fill="none" stroke="#f25c4c" stroke-width="1.1"/></svg>
      Protocols
    </div>
    <div class="setting-row">
      <svg width="12" height="10" viewBox="0 0 12 10" aria-hidden="true"><path d="M6.5 1.5A3.6 3.6 0 102 6.8M6.5 8.5A3.6 3.6 0 012 3.2" fill="none" stroke="#f25c4c" stroke-width="1.1"/><path d="M4 5h7M9 3l2 2-2 2" fill="none" stroke="#f25c4c" stroke-width="1.1"/></svg>
      Logout
    </div>
  </div>
  <nav class="legal"><a>Terms of Service</a><a>Private policy</a></nav>
</section>

<!-- Protocol selection -->
<section class="screen screen--protocols" aria-label="Protocol selection screen">
  <div class="status-bar">
    <span class="status-bar__time">9:41</span>
    <svg class="status-bar__icons" width="30" height="7" viewBox="0 0 30 7" aria-hidden="true">
      <rect x="0" y="5" width="1.4" height="2"/><rect x="2.2" y="3.5" width="1.4" height="3.5"/><rect x="4.4" y="2" width="1.4" height="5"/><rect x="6.6" y="0.5" width="1.4" height="6.5"/>
      <path d="M13.5 6.5l-1.2-1.3a1.8 1.8 0 012.4 0zM11.4 4.3a3 3 0 014.2 0l.6-.7a4 4 0 00-5.4 0zM10.2 3a4.8 4.8 0 016.6 0l.6-.7a5.8 5.8 0 00-7.8 0z"/>
      <rect x="19.5" y="0.8" width="9" height="5.4" rx="1.2" fill="none" stroke="#111" stroke-width="0.7"/><rect x="20.5" y="1.8" width="7" height="3.4" rx="0.5"/><rect x="29" y="2.6" width="0.8" height="1.8"/>
    </svg>
  </div>
  <div class="nav-bar">
    <span class="nav-bar__back"><svg width="4" height="7" viewBox="0 0 4 7" aria-hidden="true"><path d="M3.5 .5L.8 3.5l2.7 3" fill="none" stroke="#2f7cf6" stroke-width="0.9"/></svg>Settings</span>
    <div class="nav-bar__title">Protocols</div>
  </div>
  <h2 class="section-title">Protocol Selection</h2>
  <ul class="protocol-list">
    <li class="protocol"><span class="protocol__name">AUTOMATIC</span><span class="protocol__desc">Let Nestra VPN choose the best Protocol</span></li>
    <li class="protocol"><span class="protocol__name">IPSec</span><span class="protocol__desc">The most secure Protocol</span></li>
    <li class="protocol"><span class="protocol__name">IKEv2</span><span class="protocol__desc">The most stable Protocol</span></li>
  </ul>
</section>

</body>
</html>
```